Childcare Centre Franchise Website Design

Our business is Childcare centre, and we are the franchise with 4 centres currently, we would like to have the website similar as the link below,
https://www.maplewren.edu.au/
with the same items, functions and pages. Locations information for all centres, and have pages for each centre. Additionally, we will need a page for online enrolment.
Our logo is attached.

```html
<!DOCTYPE html>
<html lang="en">
<head>
<meta charset="utf-8">
<title>Little Acorns Childcare</title>
<link href="https://fonts.googleapis.com/css2?family=Signika:wght@400;600;700&family=Montserrat:wght@400;500;600;700&family=Archivo+Black&display=swap" rel="stylesheet">
<style>
:root{
  --orange:#f0522b;
  --navy:#1e3a4a;
  --footer:#1f3f4c;
  --peach:#f9e7dd;
  --peach-soft:#fcefe8;
  --text:#3b3b3b;
  --muted:#555;
  --white:#fff;
}
*{margin:0;padding:0;box-sizing:border-box}
html,body{width:1200px;height:4952px;overflow:hidden}
body{position:relative;background:var(--white);font-family:"Montserrat",sans-serif;color:var(--text)}
.abs{position:absolute}
.ph{display:block}
h1,h2,h3{font-family:"Signika",sans-serif;color:var(--navy)}
.btn-outline{display:inline-block;border:1.5px solid var(--orange);color:var(--orange);border-radius:20px;font-size:11px;padding:5px 12px}
.btn-solid{display:inline-block;background:var(--orange);color:#fff;border-radius:30px;font-size:11px;font-weight:600;padding:3px 18px}

/* hero */
.hero{left:0;top:0;width:1200px;height:730px;overflow:hidden}
.hero-photo{position:absolute;inset:0;background:linear-gradient(120deg,#2c2a33 0%,#5c4a44 35%,#8a6f5c 60%,#3c4860 85%,#2a2a3a 100%)}
.hero-shade{position:absolute;inset:0;background:linear-gradient(90deg,rgba(20,20,25,.75),rgba(20,20,25,.2) 70%)}
.logo{left:96px;top:14px;width:104px;text-align:center}
.logo-dot{width:38px;height:38px;border-radius:50%;background:#6a8a3a;margin:0 auto 6px}
.logo-name{font-family:"Signika",sans-serif;font-weight:600;color:#e0733c;font-size:13px;letter-spacing:.5px}
.top-search{left:742px;top:40px;width:304px;height:28px;background:#fff;border-radius:14px}
.top-search span{position:absolute;left:14px;top:8px;font-size:9px;color:#bbb}
.top-search b{position:absolute;right:0;top:0;height:28px;width:88px;background:var(--orange);border-radius:14px;color:#fff;font-size:11px;font-weight:600;text-align:center;line-height:28px}
.menu{left:1072px;top:43px}
.hero-title{left:100px;top:162px;font-family:"Archivo Black",sans-serif;color:#fff;font-size:52px;line-height:73px;letter-spacing:1px}
.hero-copy{left:100px;top:380px;width:540px;color:#fff;font-size:13.5px;line-height:22px;font-weight:500}
.enrol{left:100px;top:486px;color:#fff;font-size:15px;font-weight:700}
.hero-search{left:100px;top:520px;width:305px;height:28px;background:#fff;border-radius:14px}
.hero-search span{position:absolute;left:16px;top:8px;font-size:9px;color:#bbb}
.hero-search b{position:absolute;right:0;top:0;height:28px;width:100px;background:var(--navy);border-radius:14px;color:#fff;font-size:11px;font-weight:600;text-align:center;line-height:28px}
.location{left:100px;top:556px;color:#ddd;font-size:10px}
.wave{left:0;top:700px}

/* support */
.sec-title{left:0;width:1200px;text-align:center;font-size:38px;font-weight:600}
.sec-sub{left:0;width:1200px;text-align:center;font-size:12px;font-weight:600;line-height:20px;color:#333}
.support-card{top:962px;width:300px;height:306px;text-align:center;padding-top:32px;border-radius:10px}
.support-card.active{background:var(--peach)}
.icon-box{width:86px;height:68px;border:1.5px solid #c7c7c7;background:#fff;margin:0 auto 26px;border-radius:3px;display:flex;align-items:center;justify-content:center}
.support-card h3{font-family:"Montserrat",sans-serif;font-size:16px;font-weight:700;margin-bottom:16px}
.support-card p{font-size:13.5px;line-height:19px;color:#666;width:230px;margin:0 auto 16px}

/* culture */
.culture-title{left:100px;top:1382px;font-size:38px;line-height:52px;font-weight:600}
.culture-copy{left:100px;top:1504px;width:490px;font-size:12.5px;line-height:19px;color:#444}
.culture-copy p{margin-bottom:18px}
.read-more{left:100px;top:1702px;width:176px;height:52px;border-radius:26px;background:var(--orange);color:#fff;font-size:14px;font-weight:600;text-align:center;line-height:52px}
.circle{border-radius:50%;border:7px solid #fbe9e1;box-shadow:0 6px 16px rgba(0,0,0,.12)}

/* love of */
.love-card{top:2208px;width:333px;height:254px;background:var(--peach);border-radius:8px;text-align:center;padding-top:58px}
.love-card h3{font-family:"Montserrat",sans-serif;font-size:16px;font-weight:700;line-height:23px;margin-bottom:14px}
.love-card p{font-size:13.5px;line-height:19px;color:#444;width:270px;margin:0 auto 12px}
.love-photo{top:2010px;width:246px;height:246px}

/* news */
.news-card{top:2667px;width:322px;height:425px;background:var(--peach);border-radius:8px;padding:20px 18px}
.news-photo{width:286px;height:162px;margin-bottom:30px}
.news-card h3{font-family:"Montserrat",sans-serif;font-size:15px;font-weight:700;line-height:21px;margin:0 8px 18px}
.news-card p{font-size:13px;line-height:18px;color:#444;margin:0 8px 18px;width:270px}
.news-card .btn-outline{margin-left:8px;border-color:#555;color:#555;padding:6px 16px}

/* village */
.village-sub{left:0;width:1200px;text-align:center;top:3238px;font-size:20px;font-weight:600;color:#555}
.state{left:0;width:1200px;text-align:center;font-family:"Signika",sans-serif;font-size:28px;font-weight:600;color:var(--orange);text-decoration:underline;text-underline-offset:4px}
.centre-card{width:420px;height:167px;background:var(--peach-soft);display:flex;box-shadow:0 4px 14px rgba(0,0,0,.12)}
.centre-photo{width:167px;height:167px}
.centre-text{flex:1;text-align:center;padding:38px 18px 0;font-size:11.5px;line-height:15px;color:#444}
.centre-text b{display:block;margin-top:12px;color:#111;font-size:12px}

/* be bold */
.bold-wrap{left:148px;top:4106px;width:904px;height:378px;border:2px dashed #e4dcd4;border-radius:189px;padding:12px}
.bold-inner{width:100%;height:100%;background:#e8dfd3;border-radius:180px;position:relative;overflow:hidden}
.bold-photo{position:absolute;left:60px;top:-8px;width:300px;height:366px;border-radius:150px 150px 0 0}
.bold-text{position:absolute;left:410px;top:110px;width:420px}
.bold-text h2{color:var(--orange);font-size:34px;font-weight:600;line-height:38px}
.bold-text p{font-size:14px;line-height:19px;color:#222;margin:4px 0 22px;font-weight:500}
.bold-text span{display:inline-block;border:2px solid var(--navy);border-radius:22px;padding:6px 22px;font-size:14px;font-weight:600;color:var(--navy)}

/* footer */
.footer{left:0;top:4577px;width:1200px;height:375px;background:var(--footer);color:#fff}
.f-col{position:absolute;top:70px}
.f-col h4{font-family:"Signika",sans-serif;font-size:22px;font-weight:600;margin-bottom:24px}
.f-col li{list-style:none;font-size:12.5px;line-height:30px;color:#e6e6e6;display:flex;align-items:center;gap:10px;white-space:nowrap}
.socials{display:flex;gap:8px;margin-top:14px}
.socials span{width:34px;height:34px;border:2px solid #fff;border-radius:50%;display:flex;align-items:center;justify-content:center}
.socials i{width:10px;height:10px;background:#fff;border-radius:50%}
.gallery{display:grid;grid-template-columns:repeat(3,72px);gap:8px}
.gallery div{height:68px;border:2px solid #fff}
.news-form{margin-top:20px;width:230px;height:52px;border:2px solid #fff;border-radius:4px;position:relative}
.news-form span{position:absolute;left:24px;top:16px;font-size:12px;color:#ddd}
.news-form b{position:absolute;right:8px;top:8px;height:32px;padding:0 14px;background:var(--orange);border-radius:16px;font-size:12px;font-weight:500;line-height:32px}
.copy-line{position:absolute;left:60px;right:60px;top:340px;border-top:1px solid rgba(255,255,255,.4);padding-top:10px;display:flex;justify-content:space-between;font-size:12.5px}
.legal span{padding:0 14px;border-left:1px solid #fff}
.legal span:first-child{border-left:none}
</style>
</head>
<body>

<section class="hero abs">
  <div class="hero-photo" role="img" aria-label="Photo of a toddler playing with picture cards on a table"></div>
  <div class="hero-shade"></div>
</section>
<div class="logo abs"><div class="logo-dot"></div><div class="logo-name">LITTLE ACORNS</div></div>
<div class="top-search abs"><span>Find a Centre</span><b>Search</b></div>
<svg class="menu abs" width="30" height="22" viewBox="0 0 30 22"><g stroke="#fff" stroke-width="2.5" stroke-linecap="round"><line x1="2" y1="3" x2="28" y2="3"/><line x1="2" y1="11" x2="28" y2="11"/><line x1="12" y1="19" x2="28" y2="19"/></g></svg>
<h1 class="hero-title abs">WE ARE REALLY<br>CARE ABOUT YOUR<br>CHILD’S HEALTH</h1>
<p class="hero-copy abs">lorem ipsum dolor sit amet, consectetur adipiscing elit, sed do eiusmod tempor incididunt ut labore et dolore magna aliqua. ut enim ad minim veniam, quis nostrud exercitation ullamco laboris nisi ut aliquip ex ea commodo consequat.</p>
<div class="enrol abs">FIND MORE CENTRE TO ENROL</div>
<div class="hero-search abs"><span>Enter Postcode Or Suburb</span><b>Search</b></div>
<div class="location abs">Or use your current location</div>
<svg class="wave abs" width="1200" height="40" viewBox="0 0 1200 40">
  <path fill="#fff" d="M0 40 L0 22 Q25 0 50 22 Q75 0 100 22 Q125 0 150 22 Q175 0 200 22 Q225 0 250 22 Q275 0 300 22 Q325 0 350 22 Q375 0 400 22 Q425 0 450 22 Q475 0 500 22 Q525 0 550 22 Q575 0 600 22 Q625 0 650 22 Q675 0 700 22 Q725 0 750 22 Q775 0 800 22 Q825 0 850 22 Q875 0 900 22 Q925 0 950 22 Q975 0 1000 22 Q1025 0 1050 22 Q1075 0 1100 22 Q1125 0 1150 22 Q1175 0 1200 22 L1200 40 Z"/>
</svg>

<h2 class="sec-title abs" style="top:836px">We’re Here To Support The Whole Family</h2>
<p class="sec-sub abs" style="top:888px">It Is A Long Established Fact That A Reader Will Be Distracted By The Readable<br>Content Of A Page When Looking At Its Layout.</p>

<div class="support-card abs" style="left:128px">
  <div class="icon-box"><svg width="40" height="40" viewBox="0 0 40 40"><circle cx="20" cy="22" r="11" fill="#f4b98c"/><circle cx="28" cy="10" r="4" fill="#e44"/></svg></div>
  <h3>Child Care Subsidy</h3><p>Our Fast &amp; Simple Child Care Subsidy Calculator Can Help You Determine What Support You’re Eligible For.</p>
  <span class="btn-outline">Calculate Your CCS</span>
</div>
<div class="support-card active abs" style="left:450px">
  <div class="icon-box"><svg width="40" height="40" viewBox="0 0 40 40"><text x="6" y="30" font-size="28" font-weight="700" fill="#3a7bd5" font-family="sans-serif">?</text><text x="20" y="30" font-size="24" font-weight="700" fill="#f0a020" font-family="sans-serif">?</text></svg></div>
  <h3>Why Maplewren?</h3><p>Our Fast &amp; Simple Child Care Subsidy Calculator Can Help You Determine What Support You’re Eligible For.</p>
  <span class="btn-outline">Calculate Your CCS</span>
</div>
<div class="support-card abs" style="left:772px">
  <div class="icon-box"><svg width="40" height="40" viewBox="0 0 40 40"><path d="M20 34 L6 20 A8 8 0 0 1 20 10 A8 8 0 0 1 34 20 Z" fill="#e8465a"/></svg></div>
  <h3>Health &amp; Wellbeing</h3><p>Our Fast &amp; Simple Child Care Subsidy Calculator Can Help You Determine What Support You’re Eligible For.</p>
  <span class="btn-outline">Calculate Your CCS</span>
</div>

<h2 class="culture-title abs">Kearn More About Our Work And<br>Our Cultural Activities</h2>
<div class="culture-copy abs">
  <p>It Is A Long Established Fact That A Reader Will Be Distracted By The Readable Content Of A Page When Looking At Its Layout. The Point Of Using Lorem Ipsum .</p>
  <p>Is That It Has A More-Or-Less Normal Distribution Of Letters, As Opposed To Using ‘Content Here, Content Here’, Making It Look Like Readable English. Many Desktop Publishing Packages And Web Page Editors Now Use Lorem Ipsum As Their Default Model Text, And A Search For ‘lorem Ipsum’ Will Uncover Many Web Sites Still In Their Infancy.</p>
</div>
<div class="read-more abs">READ MORE</div>
<div class="circle abs" style="left:730px;top:1343px;width:366px;height:366px;background:linear-gradient(160deg,#f2efee,#d9c9c0 60%,#b08a70)" role="img" aria-label="Photo of a smiling young girl"></div>
<div class="circle abs" style="left:670px;top:1580px;width:236px;height:236px;background:linear-gradient(150deg,#3b9fe0,#f5e31a 55%,#e23a3a)" role="img" aria-label="Photo of a child crawling through a colourful play tunnel"></div>
<div class="circle abs" style="left:930px;top:1580px;width:236px;height:236px;background:linear-gradient(150deg,#e6dad0,#c46a8a 55%,#5d7fb0)" role="img" aria-label="Photo of a child looking through a toy camera"></div>

<h2 class="sec-title abs" style="top:1878px">A Love Of</h2>
<p class="sec-sub abs" style="top:1934px">It Is A Long Established Fact That A Reader Will Be Distracted By The Readable<br>Content Of A Page When Looking At Its Layout.</p>

<div class="love-card abs" style="left:82px"><h3>HIGH QUALITY<br>CURRICULUM</h3><p>It Is A Long Established Fact That A Reader Will Be Distracted By The Readable Content Of A Page When Looking At Its Layout.</p><span class="btn-solid">READ MORE</span></div>
<div class="love-card abs" style="left:433px"><h3>EXCITING<br>ENVIRONMENTS</h3><p>It Is A Long Established Fact That A Reader Will Be Distracted By The Readable Content Of A Page When Looking At Its Layout.</p><span class="btn-solid">READ MORE</span></div>
<div class="love-card abs" style="left:784px"><h3>WELLBEING &amp;<br>NUTRITION</h3><p>It Is A Long Established Fact That A Reader Will Be Distracted By The Readable Content Of A Page When Looking At Its Layout.</p><span class="btn-solid">READ MORE</span></div>
<div class="love-photo circle abs" style="left:125px;background:linear-gradient(160deg,#f3eeee,#e8c8b8 50%,#3a6ec8)" role="img" aria-label="Photo of a girl drawing at a desk"></div>
<div class="love-photo circle abs" style="left:476px;background:linear-gradient(160deg,#7ccbe8,#f0c030 55%,#3a5aa0)" role="img" aria-label="Photo of a group of children sitting together"></div>
<div class="love-photo circle abs" style="left:827px;background:linear-gradient(160deg,#dfe6ea,#6b4a3a 50%,#e07a3a)" role="img" aria-label="Photo of a boy painting at a table"></div>

<h2 class="sec-title abs" style="top:2546px;font-family:'Montserrat',sans-serif;font-weight:600;font-size:31px">LATEST NEWS &amp; ADVICE FROM OUR TEAM OF EXPERTS</h2>
<p class="sec-sub abs" style="top:2594px">It Is A Long Established Fact That A Reader Will Be Distracted By The Readable<br>Content Of A Page When Looking At Its Layout.</p>

<div class="news-card abs" style="left:100px"><div class="news-photo ph" style="background:linear-gradient(140deg,#a8553a,#e0b040 50%,#3a8a5a)" role="img" aria-label="Photo of children at a craft table"></div><h3>10 SIGNS YOUR CHILD MIGHT BE READY FOR SCHOOL</h3><p>each year around this time, our centres begin to have conversations and meetings with parents who are still deciding whether to send.....</p><span class="btn-outline">READ MORE</span></div>
<div class="news-card abs" style="left:438px"><div class="news-photo ph" style="background:linear-gradient(140deg,#3a4a3a,#d8c060 45%,#f0d0b0)" role="img" aria-label="Photo of a toddler stacking letter blocks"></div><h3>RISKY BUSINESS: APPROPRIATE RISKS DURING PLAY</h3><p>taking risks is an important part of life. it’s also important in the development of children. by taking appropriate risks.....</p><span class="btn-outline">READ MORE</span></div>
<div class="news-card abs" style="left:778px"><div class="news-photo ph" style="background:linear-gradient(140deg,#3a1a4a,#c03060 40%,#f0b030 75%,#5a8ad0)" role="img" aria-label="Photo of colourful crayons in a box"></div><h3>MEET HANNAH - CENTRE MANAGER AT MAPLEWREN ELMWOOD PARK</h3><p>hannah, centre manager of our elmwood park centre, is an incredible leader and a valued member of our maplewren.....</p><span class="btn-outline">READ MORE</span></div>

<h2 class="sec-title abs" style="top:3182px">Find Your Village</h2>
<p class="village-sub abs">Childcare Centres By State</p>

<div class="state abs" style="top:3300px">Victoria</div>
<div class="centre-card abs" style="left:140px;top:3356px"><div class="centre-photo" style="background:linear-gradient(180deg,#9ab8d0,#6a8aa8 50%,#e8eef2)" role="img" aria-label="Photo of a ferry in front of a city skyline"></div><div class="centre-text">It Is A Long Established Fact That A Reader Will Be Distracted By The Readable Content Of A Page When Looking At Its Layout.<b>LOREM IPSUM</b></div></div>
<div class="centre-card abs" style="left:640px;top:3356px"><div class="centre-photo" style="background:linear-gradient(180deg,#b8c8d8,#5a7a6a 55%,#3a4a3a)" role="img" aria-label="Photo of a coastal town at dusk"></div><div class="centre-text">It Is A Long Established Fact That A Reader Will Be Distracted By The Readable Content Of A Page When Looking At Its Layout.<b>LOREM IPSUM</b></div></div>

<div class="state abs" style="top:3546px">New South Wales</div>
<div class="centre-card abs" style="left:140px;top:3602px"><div class="centre-photo" style="background:linear-gradient(180deg,#8ab0d8,#4a7a5a 50%,#2a5a8a)" role="img" aria-label="Photo of coastal cliffs and the sea"></div><div class="centre-text">It Is A Long Established Fact That A Reader Will Be Distracted By The Readable Content Of A Page When Looking At Its Layout.<b>LOREM IPSUM</b></div></div>
<div class="centre-card abs" style="left:640px;top:3602px"><div class="centre-photo" style="background:linear-gradient(180deg,#7a8a9a,#4a5a6a 50%,#b86a4a)" role="img" aria-label="Photo of a harbour town beneath hills"></div><div class="centre-text">It Is A Long Established Fact That A Reader Will Be Distracted By The Readable Content Of A Page When Looking At Its Layout.<b>LOREM IPSUM</b></div></div>

<div class="state abs" style="top:3792px">Queenland</div>
<div class="centre-card abs" style="left:140px;top:3848px"><div class="centre-photo" style="background:linear-gradient(180deg,#9ac0e0,#e8e4dc 55%,#4a7aa0)" role="img" aria-label="Photo of a harbour opera building"></div><div class="centre-text">It Is A Long Established Fact That A Reader Will Be Distracted By The Readable Content Of A Page When Looking At Its Layout.<b>LOREM IPSUM</b></div></div>
<div class="centre-card abs" style="left:640px;top:3848px"><div class="centre-photo" style="background:linear-gradient(180deg,#1a2030,#8a4a3a 55%,#2a3040)" role="img" aria-label="Photo of a city river at night"></div><div class="centre-text">It Is A Long Established Fact That A Reader Will Be Distracted By The Readable Content Of A Page When Looking At Its Layout.<b>LOREM IPSUM</b></div></div>

<div class="bold-wrap abs">
  <div class="bold-inner">
    <div class="bold-photo" style="background:linear-gradient(170deg,#e8c8a0,#f0d8d0 45%,#e890b8)" role="img" aria-label="Photo of a smiling girl giving a thumbs up"></div>
    <div class="bold-text">
      <h2>Be Bold</h2>
      <p>Childcare Is More Than A Career At Maplewren<br>Children Are The Heart Of Our Centres &amp; Our People<br>Are The Soul.</p>
      <span>Careers At Maplewren</span>
    </div>
  </div>
</div>

<footer class="footer abs">
  <div class="f-col" style="left:76px">
    <h4>Get In Touch</h4>
    <ul>
      <li><svg width="12" height="14" viewBox="0 0 12 14"><path d="M6 13 C2 8 1 6 1 5 A5 5 0 0 1 11 5 C11 6 10 8 6 13Z" fill="none" stroke="#fff" stroke-width="1.3"/><circle cx="6" cy="5" r="1.6" fill="#fff"/></svg>48 Wattle Lane, Elmwood VIC</li>
      <li><svg width="13" height="13" viewBox="0 0 13 13"><path d="M2 1 L5 1 L6 4 L4 5 Q5 8 8 9 L9 7 L12 8 L12 11 Q6 13 2 7 Q0 4 2 1Z" fill="none" stroke="#fff" stroke-width="1.2"/></svg>+61 3 9000 4172</li>
      <li><svg width="14" height="11" viewBox="0 0 14 11"><rect x="1" y="1" width="12" height="9" fill="none" stroke="#fff" stroke-width="1.2"/><path d="M1 1 L7 6 L13 1" fill="none" stroke="#fff" stroke-width="1.2"/></svg>hello@maplewren.au</li>
    </ul>
    <div class="socials"><span><i></i></span><span><i></i></span><span><i></i></span><span><i></i></span></div>
  </div>
  <div class="f-col" style="left:350px">
    <h4>Quick Links</h4>
    <ul><li>› About us</li><li>› Contact us</li><li>› Our Services</li><li>› Privacy Policy</li><li>› Term 7 Condition</li></ul>
  </div>
  <div class="f-col" style="left:622px">
    <h4>Photo Gallery</h4>
    <div class="gallery">
      <div style="background:linear-gradient(160deg,#8aa0c0,#3a4a6a)" role="img" aria-label="Gallery photo of a harbour"></div>
      <div style="background:linear-gradient(160deg,#5a8ad0,#1a3a7a)" role="img" aria-label="Gallery photo of city towers"></div>
      <div style="background:linear-gradient(160deg,#c08ad0,#e05a3a)" role="img" aria-label="Gallery photo of a city at sunset"></div>
      <div style="background:linear-gradient(160deg,#2a3a5a,#6a8ab0)" role="img" aria-label="Gallery photo of a city at night"></div>
      <div style="background:linear-gradient(160deg,#3a2a6a,#a05ac0)" role="img" aria-label="Gallery photo of city lights"></div>
      <div style="background:linear-gradient(160deg,#8a9ad0,#c0a0c0)" role="img" aria-label="Gallery photo of a skyline at dusk"></div>
    </div>
  </div>
  <div class="f-col" style="left:896px">
    <h4>Newsletter</h4>
    <p style="font-size:12.5px;line-height:16px;color:#e6e6e6;width:230px">dolar amet sit justo amet elitr clita ipsum elitr est.</p>
    <div class="news-form"><span>Your email</span><b>sign up</b></div>
  </div>
  <div class="copy-line">
    <span>Copyright © 2023 Northbeam All Rights Reserved.</span>
    <span class="legal"><span>Home</span><span>Cookies</span><span>Help</span><span>FAQs</span></span>
  </div>
</footer>

</body>
</html>
```